VELDA Metals - newly established Metal trading business

Velda Metals is a newly established Metal trading, processing and refining business

we are looking for a simple and professional business website, which is easy to navigate

We will be selling metal / commodities to some of the largest industrial business globally. Therefore the website must make us look like a large and reputable business.

We have attached a Powerpoint presentation with some ideas

Target Market(s)

Lagre metal consumers

Industry/Entity Type

Commodity

Logo Text

VELDA Metals Group

Coding

Coded - Design and coding required

Number of Pages Required

5+ page

Font styles to use
Sans Serif

Colors

Designer to choose colors to be used in the design.

Requirements
Must have
• - fixed menu bar at the top
• - continuous scroll down function
• - multiple tabs left and right for more information
• - have dynamic screen size adjustment / a mobile version
• - google maps

```html
<!DOCTYPE html>
<html lang="en">
<head>
<meta charset="utf-8">
<title>VELDA Metals Group</title>
<link href="https://fonts.googleapis.com/css2?family=Open+Sans:wght@400;600;700;800&display=swap" rel="stylesheet">
<style>
:root{
  --navy:#1f2532;
  --navy-deep:#1a1f2b;
  --orange:#f07a1a;
  --ink:#1e222b;
  --text:#3a3d44;
  --white:#ffffff;
  --line:#d9d9d9;
  --social:#1d6fc4;
}
*{margin:0;padding:0;box-sizing:border-box}
html,body{width:1200px;height:3965px;overflow:hidden}
body{position:relative;font-family:"Open Sans",Arial,sans-serif;color:var(--text);background:var(--white)}
.abs{position:absolute}

/* header */
.site-header{left:0;top:0;width:1200px;height:79px;background:var(--navy)}
.brand{display:flex;align-items:center;gap:8px;color:var(--white);font-weight:800;font-size:17px;letter-spacing:1px;line-height:1.05}
.brand .dot{width:14px;height:14px;border-radius:50%;background:var(--orange);flex:none}
.brand small{display:block;font-size:9px;letter-spacing:2px}
.site-header .brand{left:132px;top:20px}
.main-nav{left:555px;top:31px;display:flex;gap:0}
.main-nav a{color:var(--white);font-size:12px;font-weight:700;text-decoration:none;position:absolute;white-space:nowrap}
.login-btn{left:994px;top:26px;width:72px;height:28px;border-radius:5px;background:var(--orange);color:var(--white);font-size:12px;font-weight:700;text-align:center;line-height:28px}

/* hero */
.hero{left:0;top:79px;width:1200px;height:627px;background:linear-gradient(115deg,#5a3320 0%,#8a4a2c 30%,#6b3a24 55%,#3e2a22 80%,#2d2420 100%)}
.hero-title{left:143px;top:282px;width:470px;color:var(--white);font-size:24px;font-weight:700;line-height:1.3}
.step{top:412px;width:38px;height:38px;border-radius:50%;border:2px solid var(--white);color:var(--white);font-size:12px;font-weight:700;text-align:center;line-height:34px}
.step.active{background:var(--orange);border-color:var(--orange)}
.step-label{top:456px;color:var(--white);font-size:12px;font-weight:700;width:80px;text-align:center}
.step-label.active{color:var(--orange)}
.slider-dot{top:638px;width:9px;height:9px;border-radius:50%;background:var(--white)}
.slider-dot.active{background:var(--orange)}

/* about */
.about-title{left:159px;top:776px;color:var(--ink);font-size:28px;font-weight:800;line-height:1.3}
.about-col{top:888px;width:404px;font-size:12px;line-height:1.5;text-align:justify}

/* aluminium */
.commodity{left:0;top:1092px;width:1200px;height:652px;background:linear-gradient(180deg,#d3dbe3 0%,#bdc8d3 45%,#8fa2b6 72%,#3b5f8a 88%,#6c7f91 100%)}
.commodity-title{left:0;top:1136px;width:1200px;text-align:center;color:var(--ink);font-size:30px;font-weight:800}
.spec-list{list-style:none;font-size:12.5px;color:var(--ink);line-height:1.25}
.spec-list li{position:relative;padding-left:12px;margin-bottom:6px}
.spec-list li::before{content:"";position:absolute;left:0;top:4px;border-left:5px solid var(--ink);border-top:4px solid transparent;border-bottom:4px solid transparent}
.spec-list.wide li{margin-bottom:18px}
.arrow-btn{top:1296px;width:36px;height:36px}

/* services */
.section-title{left:0;top:1816px;width:1200px;text-align:center;color:var(--ink);font-size:30px;font-weight:800}
.service-card{width:455px;height:413px;background:var(--white);box-shadow:0 6px 24px rgba(0,0,0,.16)}
.service-icon{left:43px;top:36px;width:84px;height:84px;border-radius:50%;background:var(--orange)}
.service-name{left:154px;top:50px;color:var(--ink);font-size:19px;font-weight:800;line-height:1.35}
.service-text{left:43px;top:150px;width:375px;font-size:11.5px;line-height:1.5;text-align:justify}
.service-text p{margin-bottom:22px}

/* map */
.map{left:0;top:2886px;width:1200px;height:471px;background:linear-gradient(160deg,#e7e6e2 0%,#dcdcd6 50%,#e4e2dc 100%)}

/* offices */
.office{top:3409px;width:304px;height:217px;border:1px solid var(--line);text-align:center}
.office h3{margin-top:38px;color:var(--ink);font-size:14px;font-weight:800}
.office hr{width:220px;margin:12px auto 28px;border:0;border-top:1px solid var(--line)}
.office p{font-size:11.5px;line-height:1.6}
.office .tel{margin-top:22px}

/* footer */
.site-footer{left:0;top:3687px;width:1200px;height:278px;background:var(--navy-deep)}
.site-footer .brand{left:132px;top:3745px}
.footer-head{color:var(--white);font-size:12px;font-weight:700}
.footer-nav a{position:absolute;color:var(--white);font-size:11px;font-weight:600;text-decoration:none;white-space:nowrap}
.social{top:3772px;width:26px;height:26px;border-radius:50%;background:var(--social)}
.copyright{left:0;top:3898px;width:1200px;text-align:center;color:#c9ccd3;font-size:11px}
</style>
</head>
<body>

<header class="site-header abs"></header>
<div class="brand abs" style="left:132px;top:20px"><span class="dot"></span><span>VELDA<small>METALS GROUP</small></span></div>
<nav class="main-nav abs" style="left:0;top:31px;width:1200px">
  <a href="#" style="left:555px">HOME</a>
  <a href="#" style="left:624px">ABOUT</a>
  <a href="#" style="left:695px">COMMODITIES</a>
  <a href="#" style="left:817px">SERVICES</a>
  <a href="#" style="left:907px">CONTACT</a>
</nav>
<div class="login-btn abs">LOGIN</div>

<section class="hero abs" role="img" aria-label="Photograph of stacked copper pipes"></section>
<h1 class="hero-title abs">Velda Metals is a global commodities group with an established presence throughout the metal markets.</h1>
<div class="step abs" style="left:150px">1</div>
<div class="step abs" style="left:243px">2</div>
<div class="step active abs" style="left:333px">3</div>
<div class="step abs" style="left:412px">4</div>
<div class="step-label abs" style="left:129px">Source</div>
<div class="step-label abs" style="left:222px">Transport</div>
<div class="step-label active abs" style="left:312px">Store</div>
<div class="step-label abs" style="left:391px">Deliver</div>
<span class="slider-dot abs" style="left:556px"></span>
<span class="slider-dot abs" style="left:581px"></span>
<span class="slider-dot active abs" style="left:606px"></span>
<span class="slider-dot abs" style="left:631px"></span>
<span class="slider-dot abs" style="left:656px"></span>

<h2 class="about-title abs">ABOUT<br>VELDA METALS GROUP</h2>
<p class="about-col abs" style="left:159px">Velda Metals is a global commodities group with an established presence throughout the metal markets. Velda Metals has a strong focus on consolidating, processing, and trading a full range of physical metal commodities, having established both European processing facilities and trading offices. Our network of clients and partners range from international metal producers, sovereigns, independent operators and industrial consumers.</p>
<p class="about-col abs" style="left:629px">The VELDA team is entrepreneurial and builds solutions for relationships based on transparency and trust. VELDA strives to be a supplier, partner and market participant that delivers value-add services to producers and consumers of commodities by managing the market risk, operational risk and quality risk inherent in the global commodity markets.</p>

<section class="commodity abs" role="img" aria-label="Photograph of a container ship at a port under a cloudy sky"></section>
<h2 class="commodity-title abs">ALUMINIUM</h2>
<ul class="spec-list abs" style="left:436px;top:1216px">
  <li>99.7% - 99.85%<br>primary aluminium</li>
  <li>Master alloys</li>
  <li>AlMn20/25</li>
  <li>AlSi30/50</li>
  <li>AlTi10</li>
  <li>AlZr5/10</li>
  <li>AlV5/10</li>
  <li>AlBe5/10</li>
  <li>AlSr10/15</li>
</ul>
<ul class="spec-list wide abs" style="left:605px;top:1216px;width:380px">
  <li>P1020 (99.7%) Ingots,<br>Sows and T-Bars</li>
  <li>High Purity Aluminium Ingots, Sows and T-Bars (P0610, P0406, P0303 etc.)</li>
  <li>Offgrade Aluminium Ingots, Sows and T-Bars</li>
  <li>Billet</li>
  <li>Rod</li>
</ul>
<svg class="arrow-btn abs" style="left:270px" viewBox="0 0 36 36"><circle cx="18" cy="18" r="16.5" fill="none" stroke="#1e222b" stroke-width="1.5"/><path d="M20.5 12l-6 6 6 6" fill="none" stroke="#1e222b" stroke-width="2"/></svg>
<svg class="arrow-btn abs" style="left:963px" viewBox="0 0 36 36"><circle cx="18" cy="18" r="16.5" fill="none" stroke="#1e222b" stroke-width="1.5"/><path d="M15.5 12l6 6-6 6" fill="none" stroke="#1e222b" stroke-width="2"/></svg>

<h2 class="section-title abs">SERVICES</h2>

<article class="service-card abs" style="left:137px;top:1932px">
  <svg class="service-icon abs" viewBox="0 0 84 84"><circle cx="42" cy="42" r="42" fill="#f07a1a"/><g fill="#fff"><rect x="26" y="48" width="6" height="10"/><rect x="35" y="42" width="6" height="16"/><rect x="44" y="35" width="6" height="23"/><rect x="53" y="27" width="6" height="31"/></g></svg>
  <h3 class="service-name abs">TRADING &amp;<br>SOURCING</h3>
  <div class="service-text abs">
    <p>VELDA's experienced trading team has a wealth of knowledge throughout the global metal markets.</p>
    <p>VELDA sources refined metals of various grades from smelters and the associated raw materials from mines and refineries. Our partnerships and relationships with suppliers allow VELDA to provide a reliable and flexible service to customers with short and long term supply agreements and just in time spot transactions.</p>
    <p>The VELDA team is a reliable sourcing partner to secure the raw materials any industrial business needs on time, on specification and as needed. VELDA is able to access a global supplier base and optimise pricing for raw materials among its activities.</p>
  </div>
</article>

<article class="service-card abs" style="left:608px;top:1932px">
  <svg class="service-icon abs" viewBox="0 0 84 84"><circle cx="42" cy="42" r="42" fill="#f07a1a"/><g fill="none" stroke="#fff" stroke-width="5"><circle cx="36" cy="40" r="9"/><circle cx="52" cy="50" r="5"/></g><g stroke="#fff" stroke-width="4"><path d="M36 25v6M36 49v6M21 40h6M45 40h6M25 29l4 4M43 47l4 4M25 51l4-4M43 33l4-4"/></g></svg>
  <h3 class="service-name abs">PROCESSING &amp;<br>CONSOLIDATING</h3>
  <div class="service-text abs">
    <p>VELDA operates a physical processing and consolidation plant in the UK, responsible for processing and refining a wide variety of metallic scraps and alloys.</p>
    <p>VELDA operates a physical processing and consolidation plant in the UK, responsible for processing and refining a wide variety of metallic scraps and alloys.</p>
    <p>The VELDA team is a reliable sourcing partner to secure the raw materials any industrial business needs on time, on specification and as needed. VELDA is able to access a global supplier base and optimise pricing for raw materials among its activities.</p>
  </div>
</article>

<article class="service-card abs" style="left:137px;top:2373px">
  <svg class="service-icon abs" viewBox="0 0 84 84"><circle cx="42" cy="42" r="42" fill="#f07a1a"/><path d="M42 22l14 5v11c0 10-6 16-14 20-8-4-14-10-14-20V27z" fill="#fff"/><path d="M36 41l4 4 8-8" fill="none" stroke="#f07a1a" stroke-width="3"/></svg>
  <h3 class="service-name abs">OPERATIONAL<br>SECURITY</h3>
  <div class="service-text abs">
    <p>VELDA's senior leadership has experience across the commodity value chain including: risk management, marketing arrangements, commodity asset management, leadership of commodity production assets, lending to commodity producers and consumers and logistics management.</p>
    <p>VELDA aims to add value to all its partners, suppliers and customers by providing services that enhance their business profitability, optimise commodity production or manage balance sheets.</p>
  </div>
</article>

<article class="service-card abs" style="left:608px;top:2373px">
  <svg class="service-icon abs" viewBox="0 0 84 84"><circle cx="42" cy="42" r="42" fill="#f07a1a"/><g fill="none" stroke="#fff" stroke-width="3"><circle cx="42" cy="42" r="17"/><ellipse cx="42" cy="42" rx="7" ry="17"/><path d="M25 42h34M28 33h28M28 51h28"/></g></svg>
  <h3 class="service-name abs">OUTSOURCED<br>SOLUTIONS</h3>
  <div class="service-text abs">
    <p>VELDA operates a physical processing and consolidation plant in the UK, responsible for processing and refining a wide variety of metallic scraps and alloys.</p>
    <p>VELDA operates a physical processing and consolidation plant in the UK, responsible for processing and refining a wide variety of metallic scraps and alloys.</p>
    <p>The VELDA team is a reliable sourcing partner to secure the raw materials any industrial business needs on time, on specification and as needed. VELDA is able to access a global supplier base and optimise pricing for raw materials among its activities.</p>
  </div>
</article>

<section class="map abs" role="img" aria-label="Road map showing the office location"></section>
<svg class="abs" style="left:550px;top:3101px" width="24" height="34" viewBox="0 0 24 34"><path d="M12 0C5.4 0 0 5.2 0 11.6 0 20.5 12 34 12 34s12-13.5 12-22.4C24 5.2 18.6 0 12 0z" fill="#d93025"/><circle cx="12" cy="11.5" r="4.5" fill="#7a1410"/></svg>

<div class="office abs" style="left:132px"><h3>LOREM IPSUM IS SIMPLY</h3><hr><p>418 Foundry Road,<br>Millbrook, IL 60499</p><p class="tel">Tel : 555.010.0199</p></div>
<div class="office abs" style="left:447px"><h3>LOREM IPSUM IS SIMPLY</h3><hr><p>418 Foundry Road,<br>Millbrook, IL 60499</p><p class="tel">Tel : 555.010.0199</p></div>
<div class="office abs" style="left:761px"><h3>LOREM IPSUM IS SIMPLY</h3><hr><p>418 Foundry Road,<br>Millbrook, IL 60499</p><p class="tel">Tel : 555.010.0199</p></div>

<footer class="site-footer abs"></footer>
<div class="brand abs" style="left:132px;top:3745px"><span class="dot"></span><span>VELDA<small>METALS GROUP</small></span></div>
<div class="footer-head abs" style="left:407px;top:3740px">MENU</div>
<nav class="footer-nav abs" style="left:0;top:3774px;width:1200px">
  <a href="#" style="left:409px">HOME</a>
  <a href="#" style="left:466px">ABOUT</a>
  <a href="#" style="left:528px">COMMODITIES</a>
  <a href="#" style="left:627px">SERVICES</a>
  <a href="#" style="left:706px">CONTACT</a>
  <a href="#" style="left:777px">LOGIN</a>
</nav>
<div class="footer-head abs" style="left:970px;top:3740px">FOLLOW US</div>
<span class="social abs" style="left:972px"></span>
<span class="social abs" style="left:1006px"></span>
<span class="social abs" style="left:1040px"></span>
<p class="copyright abs">Copyrights © 2018 All Rights Reserved</p>

</body>
</html>
```